Stationery Design + Business Cards

Stationary (letterhead as A4 210x297mm and Letter 8.5"x11", preferably both master page + 2nd pages)

Also need business cards, standard size 50x88mm, can be vertical or horizontal.

You can use a front/back design for the business cards, or front only.

Looking at the uploaded file (dolvek, you already have that), I want it to use the first logo on the list (4 colors).

Alternative, try the grayscale version (second file).

I need the following information on the business card (in no particular order, let me know what you come up with): 

Firstname Lastlame 
Title 

Mobile +1 317-555-0147 

Velmarix, Inc. 
24819 Birchwood Ridge Pass 
Carmel, IN 46195 
Tel. +1 317-555-0182 
Fax +1 317-555-0163 

Web: www.velmarix.com 
Twitter: twitter/Velmarix or @Velmarix 
Facebook: facebook.com/Velmarix 

For letterhead, just the company name, address + phone number & fax number 

If you think the phone/fax or something else should not be on the business cards, or something could be missing, let me know.

```html
<!DOCTYPE html>
<html lang="en">
<head>
<meta charset="utf-8">
<title>Velmarix Letterhead 210x297mm</title>
<link rel="stylesheet" href="https://fonts.googleapis.com/css2?family=Source+Sans+3:wght@400;600;700&display=swap">
<style>
  :root {
    --stage: #000000;
    --paper: #ffffff;
    --label: #ffffff;
    --brand-blue: #1b4fa0;
    --brand-orange: #f07b22;
    --band-grey: #6d6e70;
    --band-text: #ffffff;
  }
  * { margin: 0; padding: 0; box-sizing: border-box; }
  html, body {
    width: 900px;
    height: 1200px;
    overflow: hidden;
    background: var(--stage);
    font-family: "Source Sans 3", "Myriad Pro", sans-serif;
  }
  .presentation {
    position: relative;
    width: 900px;
    height: 1200px;
  }
  .sheet-label {
    position: absolute;
    top: 28px;
    left: 0;
    width: 100%;
    text-align: center;
    color: var(--label);
    font-weight: 700;
    font-size: 18px;
    letter-spacing: 0.2px;
  }
  .letterhead {
    position: absolute;
    left: 61px;
    top: 61px;
    width: 781px;
    height: 1105px;
    background: var(--paper);
  }
  .brand {
    position: absolute;
    right: 48px;
    top: 72px;
    display: flex;
    align-items: center;
    gap: 10px;
  }
  .brand-dot {
    width: 26px;
    height: 26px;
    border-radius: 50%;
    background: var(--brand-orange);
  }
  .brand-name {
    color: var(--brand-blue);
    font-weight: 400;
    font-size: 46px;
    line-height: 1;
    letter-spacing: -0.3px;
  }
  .footer-band {
    position: absolute;
    left: 0;
    bottom: 0;
    width: 100%;
    height: 30px;
    background: var(--band-grey);
    color: var(--band-text);
    display: flex;
    align-items: center;
    justify-content: center;
    font-weight: 600;
    font-size: 10.5px;
    letter-spacing: 0.1px;
  }
</style>
</head>
<body>
  <main class="presentation">
    <h1 class="sheet-label">Letter Head 210x297mm</h1>
    <section class="letterhead">
      <div class="brand">
        <span class="brand-dot"></span>
        <span class="brand-name">Velmarix</span>
      </div>
      <footer class="footer-band">
        Velmarix, Inc., 24819 Birchwood Ridge Pass, Carmel, IN 46195, Tel. +1 317-555-0182, Fax +1 317-555-0163
      </footer>
    </section>
  </main>
</body>
</html>
```